Sleek business card design for digital agency.

Brief document attached for detailed description and inspiration. Looking for a minimalist sleek, cool, modern business card design.

Industry/Entity Type

Digital

```html
<!DOCTYPE html>
<html lang="en">
<head>
<meta charset="utf-8">
<title>Rivet Studio – Business Card</title>
<link href="https://fonts.googleapis.com/css2?family=Open+Sans:wght@400;600;700&display=swap" rel="stylesheet">
<style>
  :root {
    --page-bg: #e6e6ec;
    --steel-light: #e4e4e4;
    --steel-mid: #b9b9b9;
    --steel-dark: #6f6f6f;
    --ink: #141414;
    --ink-soft: #8a8a8a;
    --band: #262626;
    --band-text: #9a9a9a;
    --edge-blue: #5fb4d6;
  }
  * { box-sizing: border-box; margin: 0; padding: 0; }
  html, body {
    width: 1200px; height: 987px; overflow: hidden;
    background: var(--page-bg);
    font-family: "Open Sans", Arial, sans-serif;
  }
  .stage {
    position: relative; width: 1200px; height: 987px;
  }
  .card {
    position: absolute; left: 250px;
    width: 700px; height: 400px;
    border-radius: 34px; overflow: hidden;
    box-shadow: 0 8px 24px rgba(0,0,0,0.18);
  }
  .card--front { top: 70px; }
  .card--back { top: 517px; }
  .steel {
    position: absolute; inset: 0;
    background:
      linear-gradient(100deg, var(--steel-dark) 0%, var(--steel-mid) 30%, var(--steel-light) 55%, var(--steel-mid) 80%, var(--steel-dark) 100%);
  }
  .brand {
    position: absolute; display: flex; align-items: center; gap: 14px;
    color: var(--ink); font-weight: 700; letter-spacing: -0.5px;
  }
  .brand__dot {
    border-radius: 50%; background: var(--ink);
  }
  .card--front .brand { left: 46px; top: 38px; font-size: 54px; }
  .card--front .brand__dot { width: 36px; height: 36px; }
  .contacts {
    position: absolute; left: 50px; top: 140px;
    list-style: none; font-size: 17px; line-height: 27px; color: var(--ink-soft);
  }
  .contacts li { display: flex; align-items: center; gap: 10px; }
  .contacts svg { width: 16px; height: 16px; flex: none; }
  .contacts .square { width: 14px; height: 14px; border-radius: 2px; background: var(--ink-soft); flex: none; }
  .person {
    position: absolute; right: 56px; bottom: 96px; text-align: left;
  }
  .person__mark {
    position: absolute; right: 40px; bottom: 86px;
    width: 110px; height: 110px; border-radius: 50%;
    background: rgba(0,0,0,0.12);
  }
  .person__name { font-size: 28px; font-weight: 700; color: #2a2a2a; }
  .person__title { font-size: 22px; color: #444; }
  .address-band {
    position: absolute; left: 0; right: 0; bottom: 0; height: 72px;
    background: var(--band);
    border-top: 2px solid #555;
    display: flex; align-items: center; padding-left: 46px;
    font-size: 20px; color: var(--band-text);
  }
  .card--back .brand {
    left: 50%; top: 50%; transform: translate(-50%, -50%);
    font-size: 64px;
  }
  .card--back .brand__dot { width: 46px; height: 46px; }
</style>
</head>
<body>
<main class="stage">
  <section class="card card--front" aria-label="Business card front">
    <div class="steel" role="img" aria-label="Brushed steel texture"></div>
    <div class="brand"><span class="brand__dot"></span>Rivet Studio</div>
    <ul class="contacts">
      <li><svg viewBox="0 0 16 16"><path d="M4 1h3l1 4-2 1a9 9 0 0 0 4 4l1-2 4 1v3c0 1-1 2-2 2A13 13 0 0 1 2 3c0-1 1-2 2-2z" fill="#8a8a8a"/></svg>0400 123 456</li>
      <li><svg viewBox="0 0 16 16"><rect x="4" y="1" width="8" height="14" rx="1.5" fill="none" stroke="#8a8a8a" stroke-width="1.6"/><rect x="6" y="3" width="4" height="6" fill="#8a8a8a"/></svg>03 9000 1234</li>
      <li><svg viewBox="0 0 16 16"><rect x="1" y="3" width="14" height="10" rx="1" fill="none" stroke="#8a8a8a" stroke-width="1.6"/><path d="M1 4l7 5 7-5" fill="none" stroke="#8a8a8a" stroke-width="1.6"/></svg>dhoyle@rivetstudio.com</li>
      <li><span class="square"></span>RivetStudio</li>
      <li><span class="square"></span>@dhoyle82</li>
    </ul>
    <div class="person__mark"></div>
    <div class="person">
      <div class="person__name">Daniel Hoyle</div>
      <div class="person__title">Marketing Director</div>
    </div>
    <div class="address-band">Level 2, 18 Carden St, Westbrook NSW 2000</div>
  </section>

  <section class="card card--back" aria-label="Business card back">
    <div class="steel" role="img" aria-label="Brushed steel texture"></div>
    <div class="brand"><span class="brand__dot"></span>Rivet Studio</div>
  </section>
</main>
</body>
</html>
```